Marrow Cay Retreat Christmas wishes 2013

We require postcards designed to mail our to our clients for Christmas. We are a SURF travel company, with a high end market and like to mail our Christmas postcards to all our guests that have stayed with us through the year. Front cover will have images and text (ie Seasons Greeting) and our logo. The back will have space for TO: name & address and postage stamp. Will also have some basic text (ie The Management & Staff at Marrow Cay Retreat wish you and your family all the best for the Festive Season and New Year. We look forward to seeing you back at Marrow Cay Retreat again soon etc etc). Here is link to main image https://www.filecrate-demo.net/sh/qwmzrtpl83nvex/Rk7bPoQaZs

Target Market(s)

Our clients are mostly mature men (40-70) surfers who purchase luxury surf trips

Industry/Entity Type

Travel

Requirements
Must have
• Ocean Image (front)
Logo x 2 in same colour - Corvane & Marrow Cay Retreat (front)
Text (front)
Back to be white
Space for name & address (back)
Space for postage stamp (back)
Message (back)
Website www.corvanestays.net (back)

```html
<!DOCTYPE html>
<html lang="en">
<head>
<meta charset="utf-8">
<title>Marrow Cay Retreat – Christmas Postcard</title>
<link rel="stylesheet" href="https://fonts.googleapis.com/css2?family=Alfa+Slab+One&family=Josefin+Sans:wght@300&family=Open+Sans:wght@400&family=Oswald:wght@400&family=Varela+Round&display=swap">
<style>
  :root{
    --page:#ffffff;
    --card-black:#000000;
    --ink-white:#ffffff;
    --rule-grey:#6e6e6e;
    --muted-grey:#9a9a9a;
    --xmas-red:#c8121b;
    --xmas-deep:#6e0a0f;
    --night:#15171a;
    --snow:#eef2f2;
  }
  *{margin:0;padding:0;box-sizing:border-box}
  html,body{width:1200px;height:1000px;overflow:hidden;background:var(--page)}
  .board{position:relative;width:1200px;height:1000px}

  /* ---------- back of postcard ---------- */
  .postcard-back{position:absolute;left:16px;top:20px;width:669px;height:442px;background:var(--card-black);color:var(--ink-white)}
  .brand-mark{position:absolute;left:46px;top:222px;display:flex;align-items:center;gap:8px;white-space:nowrap;
    font-family:"Josefin Sans",sans-serif;font-weight:300;font-size:15.5px;letter-spacing:1px;color:var(--ink-white)}
  .brand-dot{width:10px;height:10px;border-radius:50%;background:var(--ink-white);flex:none}
  .greeting-message{position:absolute;left:48px;top:274px;width:272px;font-family:"Open Sans",sans-serif;font-size:13px;line-height:18px;color:var(--ink-white)}
  .divider{position:absolute;left:336px;top:36px;width:1px;height:396px;background:var(--rule-grey)}
  .return-address{position:absolute;left:322px;top:240px;width:205px;transform-origin:0 0;transform:rotate(-90deg);
    font-family:"Oswald",sans-serif;font-size:9px;line-height:12px;letter-spacing:.4px;color:var(--muted-grey);white-space:nowrap}
  .lodge-badge{position:absolute;left:356px;top:41px;width:144px;height:84px;background:var(--ink-white);color:#000;
    display:flex;flex-direction:column;align-items:center;justify-content:center;gap:4px;font-family:"Open Sans",sans-serif}
  .lodge-badge .site{font-size:13px}
  .lodge-badge .country{font-size:11px;letter-spacing:.5px}
  .stamp{position:absolute;left:561px;top:35px;width:73px;height:90px;background:var(--ink-white);padding:6px}
  .stamp-image{width:100%;height:100%;background:linear-gradient(160deg,#d9d9d9,#7d7d7d 60%,#3a3a3a)}
  .address-lines{position:absolute;left:356px;top:145px;width:278px;list-style:none}
  .address-lines li{height:20.5px;border-bottom:1px solid var(--rule-grey)}
  .contact-line{position:absolute;left:356px;top:396px;font-family:"Oswald",sans-serif;font-size:10px;color:var(--muted-grey);letter-spacing:.3px;white-space:nowrap}

  /* ---------- front of postcard ---------- */
  .postcard-front{position:absolute;left:16px;top:492px;width:669px;height:488px;overflow:hidden;
    background:linear-gradient(180deg,var(--night) 0%,#23262a 45%,#8d9192 60%,var(--snow) 72%,#dfe6e6 100%)}
  .winter-scene{position:absolute;inset:0}
  .front-brand{position:absolute;left:0;right:0;top:58px;display:flex;justify-content:center;align-items:center;gap:9px;
    font-family:"Josefin Sans",sans-serif;font-weight:300;font-size:17px;letter-spacing:1.2px;color:var(--ink-white)}
  .front-brand .brand-dot{width:11px;height:11px}
  .lodge-name{position:absolute;left:0;right:0;top:88px;text-align:center;font-family:"Varela Round",sans-serif;font-size:31px;color:var(--xmas-red);
    text-shadow:0 0 10px rgba(200,18,27,.6)}
  .headline{position:absolute;left:0;right:0;text-align:center;font-family:"Alfa Slab One",serif;color:var(--xmas-red);
    -webkit-text-stroke:4px var(--ink-white);paint-order:stroke fill;
    text-shadow:0 5px 0 var(--xmas-deep),0 8px 14px rgba(0,0,0,.45);line-height:1}
  .headline-merry{top:140px;font-size:128px;letter-spacing:2px}
  .headline-christmas{top:270px;font-size:80px;letter-spacing:1px}
</style>
</head>
<body>
<main class="board">

  <section class="postcard-back" aria-label="Postcard back">
    <div class="brand-mark"><span class="brand-dot"></span>CORVANE LODGES &amp; RESORTS</div>
    <p class="greeting-message">The Management &amp; Staff at Marrow Cay Retreat wish you and your family all the best for the festive season and New Year. We look forward to seeing you back at Marrow Cay Retreat again</p>
    <div class="divider"></div>
    <p class="return-address">1564 LOREM HARBOUR WAY KELSO BEND, CA 90000</p>
    <div class="lodge-badge"><span class="site">marrowcaystay.net</span><span class="country">indonesia</span></div>
    <div class="stamp"><div class="stamp-image" role="img" aria-label="Postage stamp photo of a penguin"></div></div>
    <ul class="address-lines"><li></li><li></li><li></li><li></li><li></li><li></li><li></li><li></li><li></li><li></li><li></li></ul>
    <p class="contact-line">1 (800) 555-0142 + LOREMSTAYS.COM + HELLO@LOREMSTAYS.COM</p>
  </section>

  <section class="postcard-front" aria-label="Postcard front">
    <div class="winter-scene" role="img" aria-label="Snowy night scene with falling snow, Santa's sleigh in the sky, reindeer and wrapped gifts in the snow"></div>
    <div class="front-brand"><span class="brand-dot"></span>CORVANE LODGES &amp; RESORTS</div>
    <p class="lodge-name">Marrow Cay Retreat</p>
    <h1 class="headline headline-merry">MERRY</h1>
    <p class="headline headline-christmas">CHRISTMAS</p>
  </section>

</main>
</body>
</html>
```